Top Producing Realtor Business Card Design

Looking for branding with my logo on all of my materials. I am a top producing real estate agent, selling expensive homes in California. I'm looking for a classy design that includes my existing logo, the company corporate logo and my photo.

Looking forward to your submissions! Thank you so much! :)

I appreciate your submissions very much!  Excellent work!  I have revised the brief to be more clear about what I think I'm looking for.  Keep the submissions coming in!!  Thank you so much :)

Target Market(s)

Wealthy home buyers and sellers in California.

Industry/Entity Type

Real Estate

Requirements
Must have
• Must include:

Homestead Pinnacle Logo

Below Homestead Pinnacle Logo it must say: Santa Clarita (Helvetica font)

Complete address: 58317 Barwick Street
Santa Clarita, CA 94687

Phone number: 415.962.3057 cell
415.740.2195 VM 5821 office

My photo

My name: Mara Quinlow (please make sure it's correct before you submit) :)

My MQ Logo (if possible please keep logo colors the same)

"Realtor" with a reserved symbol after or below my name

My license number: StaREB #07428915

My website: www.MaraQuinlow-example.com

My email: Mara@MaraQuinlow-example.com

Nice to have
• I'm open minded :) The main goal is to have the MQ logo is on all of my material. For the business cards I sort of imagine my MQ logo in the background, and I like a fade. I prefer the logo to be on the front of the card, and I like it on the back of the card too, So a two sided business card is ok.

I prefer the light blue Homestead Pinnacle Logo submitted. Please note the light blue color must closely match :)

Another idea is the business card can be in the format of the yard sign photo submitted (maybe changed into the light blue color), to possibly be a business card that looks like the yard sign. The yard sign layout must closely match the example submitted due to corporate guidelines.

Basically I'm looking for something that will tie everything together with my photo and logo so it's well branded in the clients mind. :)

Should not have
• Please keep the logo's exactly as they are, including color...no need to change.

If you choose to use the yard sign example provided for the business card, Please do not change the basic layout of the yard sign submitted, I have to follow the corporate standards.

```html
<!DOCTYPE html>
<html lang="en">
<head>
<meta charset="utf-8">
<title>Mara Quinlow — Business Card</title>
<link rel="stylesheet" href="https://fonts.googleapis.com/css2?family=Roboto+Condensed:wght@400;700&display=swap">
<style>
  :root {
    --page: #ffffff;
    --name-blue: #0b55a3;
    --panel-grey: #c8c6c7;
    --panel-blue: #5b88c6;
    --divider: #8a8a8a;
    --ink-light: #ffffff;
    --ink-dark: #1a1a1a;
    --badge-blue: #0f5aa6;
    --brand-tile: #a9c3e6;
  }
  html, body {
    margin: 0;
    width: 1200px;
    height: 1000px;
    overflow: hidden;
    background: var(--page);
    font-family: "Roboto Condensed", "Arial Narrow", sans-serif;
  }
  .card {
    position: absolute;
    left: 32px;
    top: 172px;
    width: 1142px;
    height: 650px;
  }
  .identity {
    position: absolute;
    left: 0; top: 0;
    width: 616px; height: 263px;
    background: var(--panel-grey);
  }
  .name {
    position: absolute;
    left: 20px; top: 110px;
    margin: 0;
    font-size: 96px;
    font-weight: 700;
    line-height: 1;
    color: var(--name-blue);
    letter-spacing: 0.5px;
    white-space: nowrap;
  }
  .title {
    position: absolute;
    left: 23px; top: 208px;
    margin: 0;
    font-size: 38px;
    font-weight: 400;
    line-height: 46px;
    color: var(--name-blue);
  }
  .title sup { font-size: 20px; vertical-align: 14px; line-height: 0; }
  .contact {
    position: absolute;
    left: 0; top: 263px;
    width: 616px; height: 387px;
    background: var(--panel-blue);
    color: var(--ink-light);
  }
  .contact-line {
    position: absolute;
    left: 22px;
    margin: 0;
    font-size: 26px;
    line-height: 32px;
    white-space: nowrap;
  }
  .phones { top: 8px; }
  .address { top: 94px; }
  .web { top: 148px; font-size: 21.5px; letter-spacing: -0.1px; }
  .brokerage {
    position: absolute;
    left: 32px; top: 216px;
    width: 190px;
    height: 150px;
  }
  .brokerage-mark {
    display: flex;
    align-items: center;
    justify-content: center;
    gap: 8px;
    height: 104px;
    background: var(--brand-tile);
    border-radius: 4px;
  }
  .brokerage-mark .dot {
    width: 12px; height: 12px;
    background: var(--name-blue);
  }
  .brokerage-mark span {
    font-size: 22px;
    font-weight: 700;
    line-height: 1.05;
    color: var(--name-blue);
  }
  .brokerage-office {
    position: absolute;
    left: 0; top: 128px;
    width: 190px;
    margin: 0;
    text-align: center;
    font-family: Helvetica, Arial, sans-serif;
    font-size: 15px;
    font-weight: 700;
    color: var(--ink-dark);
  }
  .agent-mark {
    position: absolute;
    left: 253px; top: 213px;
    width: 105px; height: 114px;
    background: var(--badge-blue);
    border-radius: 18px;
    display: flex;
    align-items: center;
    justify-content: center;
    font-size: 36px;
    font-weight: 700;
    color: var(--ink-light);
  }
  .license {
    position: absolute;
    right: 18px; top: 339px;
    margin: 0;
    font-size: 27px;
    line-height: 32px;
    color: var(--ink-light);
    white-space: nowrap;
  }
  .divider {
    position: absolute;
    left: 616px; top: 0;
    width: 9px; height: 650px;
    background: var(--divider);
  }
  .portrait {
    position: absolute;
    left: 625px; top: 0;
    width: 517px; height: 650px;
    background: radial-gradient(ellipse at 40% 35%, #8c8c8c 0%, #5a5a5a 45%, #1d1d1d 100%);
  }
</style>
</head>
<body>
  <main class="card">
    <section class="identity">
      <h1 class="name">Mara Quinlow</h1>
      <p class="title">Realtor<sup>®</sup></p>
    </section>
    <section class="contact">
      <p class="contact-line phones">415.962.3057 - Office • ext.5821- Office VM<br>415.740.2195 - Mobile</p>
      <p class="contact-line address">58317 Barwick Street, Santa Clarita, CA 94687</p>
      <p class="contact-line web">www.MaraQuinlow-example.com • Mara@MaraQuinlow-example.com</p>
      <div class="brokerage">
        <div class="brokerage-mark"><i class="dot"></i><span>Homestead<br>Pinnacle</span></div>
        <p class="brokerage-office">Santa Clarita</p>
      </div>
      <div class="agent-mark">MQ</div>
      <p class="license">StaREB #07428915</p>
    </section>
    <div class="divider"></div>
    <div class="portrait" role="img" aria-label="Studio portrait of the realtor against a grey mottled backdrop"></div>
  </main>
</body>
</html>
```